Label Design For "TUB LUMA". All natural liquid water treatment for hot tubs & spas.

Launching a new all natural product to the spa & hot tub market. It's an enzyme based liquid that will come in an aluminum bottle, roughly 500ml.
Allows the user to use far less harsh chemicals in their hot tub while making the water softer and smoother on your skin.

Product is called TUB LUMA. The reason for the name is that it uses zero chemicals, zero waste, zero animal testing, and zero effort to use it in your hot tub care routine.

There is no logo, icon, or font. Please feel free to use creative freedom with fonts. Looking for a bold, clean, minimal font for the name, preferably sans serif. A modern bold look that's really clean and minimal is what I'm looking for. The name itself will most likely be the logo. Feel free to spell the word zero or use the number 0 instead in the name.

All of our competition uses a white plastic bottle with a navy blue label. I would like to look completely different from them on a shelf. Something that implies it's natural and soft, and not old, clinical, and industrial.

These are eco friendly products with eco friendly packaging, but I don't want to use green or blue in the colours. Im obviously not a designer at all so please let your ideas flow. I like pastels or bold colours, even black and white. If you have better ideas, I'm open to suggestion. I have attached a couple images that show what my competition looks like and also some design looks and colours I like.

Target Market(s)

Spa & hot tub owners that use their own chemicals weekly/monthly - 80% Male / 20% Female

Industry/Entity Type

Hot Tub Chemicals & Water Care

Font styles to use
Sans Serif

Requirements
Must have
• Clean, Minimal, Modern. Sans Serif Font. The name "TUB LUMA". Mention that it's all natural, eco friendly water conditioner for hot tubs and spas.
Nice to have
• Multiple mockups with different colour pallets
Should not have
• Please not busy looking, and please no use of blue or green.

```html
<!DOCTYPE html>
<html lang="en">
<head>
<meta charset="utf-8">
<title>TUB LUMA – Label</title>
<link rel="stylesheet" href="https://fonts.googleapis.com/css2?family=Montserrat:wght@400;500&family=Quicksand:wght@400;500&display=swap">
<style>
  :root {
    --page-bg: #f3f3f3;
    --label-light: #f7f7f7;
    --label-light-edge: #dedede;
    --label-dark: #1d1d1d;
    --ink: #1e1e1e;
    --ink-inverse: #f2f2f2;
  }
  * { margin: 0; padding: 0; box-sizing: border-box; }
  html, body {
    width: 1200px;
    height: 960px;
    overflow: hidden;
    background: var(--page-bg);
  }
  .canvas {
    position: relative;
    width: 1200px;
    height: 960px;
  }
  .label {
    position: absolute;
    left: 400px;
    top: 67px;
    width: 400px;
    height: 825px;
    border-radius: 9px;
    overflow: hidden;
    background: radial-gradient(ellipse at 40% 35%, var(--label-light) 0%, #ececec 60%, var(--label-light-edge) 100%);
    color: var(--ink);
  }
  .label__wave {
    position: absolute;
    inset: 0;
    width: 400px;
    height: 825px;
  }
  .wordmark {
    position: absolute;
    left: 54px;
    top: 64px;
    font-family: "Montserrat", sans-serif;
    font-weight: 400;
    font-size: 104px;
    line-height: 98px;
    letter-spacing: -2px;
    color: var(--ink);
  }
  .wordmark__line { display: block; }
  .wordmark__line--first { padding-left: 38px; }
  .tagline {
    position: absolute;
    left: 0;
    right: 0;
    top: 297px;
    text-align: center;
    font-family: "Quicksand", sans-serif;
    font-weight: 500;
    font-size: 19px;
    line-height: 24px;
    color: var(--ink);
  }
  .benefits {
    position: absolute;
    left: 80px;
    top: 528px;
    list-style: none;
    font-family: "Quicksand", sans-serif;
    font-weight: 400;
    font-size: 21px;
    line-height: 29.5px;
    color: var(--ink-inverse);
  }
  .benefits__item {
    display: flex;
    align-items: center;
    gap: 5px;
  }
  .benefits__icon { width: 16px; height: 16px; flex: none; }
  .promise {
    position: absolute;
    left: 0;
    right: 0;
    top: 668px;
    text-align: center;
    font-family: "Quicksand", sans-serif;
    font-weight: 400;
    font-size: 21px;
    line-height: 28px;
    color: var(--ink-inverse);
  }
  .volume {
    position: absolute;
    left: 0;
    right: 0;
    top: 762px;
    text-align: center;
    font-family: "Quicksand", sans-serif;
    font-weight: 400;
    font-size: 16px;
    color: var(--ink-inverse);
  }
</style>
</head>
<body>
<main class="canvas">
  <section class="label">
    <svg class="label__wave" viewBox="0 0 400 825" aria-hidden="true">
      <path d="M0 418 C 90 470, 300 455, 400 360 L400 825 L0 825 Z" fill="var(--label-dark)"/>
      <path d="M0 433 C 40 452, 90 463, 140 466" fill="none" stroke="var(--label-light)" stroke-width="3"/>
    </svg>

    <h1 class="wordmark">
      <span class="wordmark__line wordmark__line--first">TUB</span>
      <span class="wordmark__line">LUMA</span>
    </h1>

    <p class="tagline">All natural liquid water<br>treatment for hot tubs &amp; spas.</p>

    <ul class="benefits">
      <li class="benefits__item">
        <svg class="benefits__icon" viewBox="0 0 16 16"><circle cx="8" cy="8" r="6.5" fill="none" stroke="currentColor" stroke-width="1.3"/><path d="M5 8.2 L7.2 10.3 L11 5.8" fill="none" stroke="currentColor" stroke-width="1.4"/></svg>
        Zero chemicals
      </li>
      <li class="benefits__item">
        <svg class="benefits__icon" viewBox="0 0 16 16"><circle cx="8" cy="8" r="6.5" fill="none" stroke="currentColor" stroke-width="1.3"/><path d="M5 8.2 L7.2 10.3 L11 5.8" fill="none" stroke="currentColor" stroke-width="1.4"/></svg>
        Zero waste
      </li>
      <li class="benefits__item">
        <svg class="benefits__icon" viewBox="0 0 16 16"><circle cx="8" cy="8" r="6.5" fill="none" stroke="currentColor" stroke-width="1.3"/><path d="M5 8.2 L7.2 10.3 L11 5.8" fill="none" stroke="currentColor" stroke-width="1.4"/></svg>
        Zero animal testing
      </li>
    </ul>

    <p class="promise">Zero effort to use it in your hot<br>tub care routine</p>

    <p class="volume">500 ml</p>
  </section>
</main>
</body>
</html>
```